依頼詳細
会社の名刺デザインをお願いします。シンプルで都会的なスマートなデザインを希望します。
記載項目
表面会社名役職住所電話FAXメールアドレスHP
希望イメージ
シンプル 複雑
単色 カラフル
暗い 明るい
日常 高級
遊び心 厳粛
未来的 伝統的
女性的 男性的
希望する色
赤系、青系、茶系、グレー系
すみません。ご質問していただいたファイルについてよくわからないのでとりあえずあるものを添付しました。
早速のデザイナーの方々のご提案ありがとうございます。ロゴの時も皆様どのデザインもおしゃれで粋で選択するのにとても困りました。やはりプロの方のデザインは違いますね。大変満足しております。名刺のロゴ使用ですが、あまり大きいロゴは考えておりません。シンプルで控えめだがインパクトのあるロゴを使用した名刺を考えておりますのでよろしくご提案お願いします。
■ 選んだ理由

ロゴマークとの調和、デザイン、全体的なバランスの良さで選択させていただきました。末永く利用させていただきます。

■ 提案者全員のお礼・コメント

皆様、沢山のご提案ありがとうございました。
どのご提案も素晴らしく選択させていただくのにロゴマーク選択時同様大変悩みました。
今回選択させていただかなかったランサーの方々も又次回機会がございましたらよろしくお願いいたします。

```html
<!DOCTYPE html>
<html lang="ja">
<head>
<meta charset="utf-8">
<title>株式会社ハルキタ工房 名刺</title>
<link rel="stylesheet" href="https://fonts.googleapis.com/css2?family=Noto+Serif+JP:wght@400;600&display=swap">
<style>
  :root {
    --page: #ffffff;
    --card: #ffffff;
    --ink: #1a1a1a;
    --accent: #c8201e;
    --shadow: rgba(0, 0, 0, 0.28);
    --edge: #e4e4e4;
  }
  * { margin: 0; padding: 0; box-sizing: border-box; }
  html, body {
    width: 804px;
    height: 1200px;
    overflow: hidden;
    background: var(--page);
    font-family: "Noto Serif JP", serif;
    color: var(--ink);
  }
  .sheet { position: relative; width: 804px; height: 1200px; }
  .card {
    position: absolute;
    left: 59px;
    width: 686px;
    height: 415px;
    background: var(--card);
    border: 1px solid var(--edge);
    box-shadow: 10px 12px 14px var(--shadow);
  }
  .card--front { top: 70px; }
  .card--back { top: 680px; }

  .title {
    position: absolute;
    left: 200px;
    top: 36px;
    writing-mode: vertical-rl;
    font-size: 21px;
    letter-spacing: 2px;
  }
  .name {
    position: absolute;
    left: 270px;
    top: 62px;
    writing-mode: vertical-rl;
    font-size: 64px;
    font-weight: 400;
    letter-spacing: 4px;
  }
  .name .gap { display: inline-block; height: 52px; }

  .brand {
    position: absolute;
    right: 38px;
    top: 292px;
    display: flex;
    flex-direction: column;
    align-items: center;
    gap: 6px;
  }
  .brand-dot {
    width: 52px;
    height: 52px;
    border-radius: 50%;
    background: var(--accent);
  }
  .brand-name {
    font-size: 17px;
    font-weight: 600;
    letter-spacing: 1px;
    color: var(--accent);
  }

  .contact {
    position: absolute;
    left: 48px;
    top: 94px;
    font-size: 18px;
    line-height: 46px;
    border-collapse: collapse;
  }
  .contact th {
    text-align: left;
    font-weight: 400;
    width: 112px;
    white-space: nowrap;
    padding: 0;
  }
  .contact td { padding: 0; white-space: nowrap; }
</style>
</head>
<body>
<main class="sheet">
  <section class="card card--front">
    <p class="title">代表取締役</p>
    <h1 class="name">山川<span class="gap"></span>和人</h1>
    <div class="brand">
      <span class="brand-dot"></span>
      <span class="brand-name">HARUKITA</span>
    </div>
  </section>

  <section class="card card--back">
    <table class="contact">
      <tr><th>会社名</th><td>株式会社ハルキタ工房</td></tr>
      <tr><th>住　所</th><td>千葉県緑川市見本町123-50　青葉ビル５Ｆ</td></tr>
      <tr><th>電　話</th><td>0470-55-0101</td></tr>
      <tr><th>ＦＡＸ</th><td>0470-55-0102</td></tr>
      <tr><th>メール</th><td>info.harukita@example.com</td></tr>
      <tr><th>Ｈ　Ｐ</th><td>http://www.harukita.example</td></tr>
    </table>
  </section>
</main>
</body>
</html>
```